Flyer für Bikeshop
Zielgruppe
Bikeshop bikevermietung bikereparatur 365/365 offen
Aufgabenstellung
Der beigelegte Flyer sollte professionell gestaltet werden. Gerne sende ich diverse Fotos mit um sie evtl. zu verwenden. Ich habe keine präferenzen. Der Flyer sollte Jugendliche ansprechen. Der Flyer kann auch gänzlich ohne Fotos sein.

```html
<!DOCTYPE html>
<html lang="de">
<head>
<meta charset="utf-8">
<title>Radwerk Alpin – Flyer Fahrtraining</title>
<link rel="stylesheet" href="https://fonts.googleapis.com/css2?family=Roboto+Slab:wght@600;700;800&family=Bebas+Neue&display=swap">
<style>
  :root {
    --page-bg: #f2efe8;
    --sand: #ede3cc;
    --espresso: #200202;
    --rust: #6b2405;
    --white: #ffffff;
    --photo-sky: #8fa3bd;
    --photo-ground: #7d7456;
    --photo-faint: #cfc7a8;
  }
  html, body {
    margin: 0;
    width: 1200px;
    height: 1200px;
    overflow: hidden;
    background: var(--page-bg);
  }
  .flyer-pair {
    position: absolute;
    top: 237px;
    left: 55px;
    display: flex;
    gap: 50px;
  }
  .flyer {
    width: 520px;
    height: 726px;
    display: block;
  }
  .headline {
    font-family: "Roboto Slab", Georgia, serif;
    font-weight: 700;
    font-size: 44px;
    fill: var(--white);
  }
  .brand-name {
    font-family: "Roboto Slab", Georgia, serif;
    font-weight: 800;
    font-size: 21px;
    letter-spacing: 5px;
    fill: var(--white);
  }
  .info-text {
    font-family: "Bebas Neue", "Arial Narrow", sans-serif;
    font-size: 15px;
    fill: var(--white);
  }
  .contact-text {
    font-family: "Roboto Slab", Georgia, serif;
    font-weight: 600;
    font-size: 14px;
    fill: var(--white);
  }
</style>
</head>
<body>
<main class="flyer-pair">

  <!-- Vorderseite -->
  <svg class="flyer flyer-front" viewBox="0 0 447 624" xmlns="http://www.w3.org/2000/svg">
    <defs>
      <linearGradient id="photoMountain" x1="0" y1="0" x2="0" y2="1">
        <stop offset="0" stop-color="var(--photo-sky)"/>
        <stop offset="1" stop-color="var(--photo-ground)"/>
      </linearGradient>
      <linearGradient id="photoTrail" x1="0" y1="0" x2="1" y2="1">
        <stop offset="0" stop-color="#7f95b0"/>
        <stop offset="1" stop-color="#8d8366"/>
      </linearGradient>
    </defs>
    <rect class="flyer-bg" width="447" height="624" fill="var(--sand)"/>

    <polygon class="corner-shape" points="0,0 12,0 84,72 0,156" fill="var(--espresso)"/>
    <polygon class="accent-diamond" points="22,168 44,190 22,212 0,190" fill="var(--rust)"/>
    <polygon class="accent-diamond" points="412,10 435,33 412,56 389,33" fill="var(--rust)"/>

    <polygon class="photo photo-ridge" role="img" aria-label="Foto: Mountainbiker auf einem Bergkamm über einem See" points="158,63 315,220 158,377 0,220" fill="url(#photoMountain)"/>
    <polygon class="photo photo-trail" role="img" aria-label="Foto: Biker auf steinigem Pfad mit Bergsee im Hintergrund" points="200,86 286,0 390,0 447,57 447,72 324,205" fill="url(#photoTrail)"/>
    <polygon class="photo photo-forest" role="img" aria-label="Foto: Biker mit Helm in einer Kurve zwischen Bäumen" points="418,138 447,167 447,480 422,505 300,383" fill="url(#photoTrail)"/>

    <rect class="headline-band" x="0" y="270" width="315" height="57" fill="var(--rust)"/>
    <text class="headline" x="18" y="314">Free Bicycle</text>
    <rect class="headline-band" x="0" y="340" width="345" height="58" fill="var(--rust)"/>
    <text class="headline" x="18" y="385">Skills Training</text>

    <polygon class="accent-triangle" points="0,408 70,478 0,548" fill="var(--rust)"/>

    <polygon class="base-panel" points="0,578 178,400 268,400 447,578 447,624 0,624" fill="var(--espresso)"/>
    <line x1="0" y1="586" x2="186" y2="400" stroke="var(--sand)" stroke-width="0.6"/>
    <line x1="260" y1="400" x2="447" y2="586" stroke="var(--sand)" stroke-width="0.6"/>

    <text class="brand-name" x="223" y="536" text-anchor="middle">RADWERK ALPIN</text>
  </svg>

  <!-- Rückseite -->
  <svg class="flyer flyer-back" viewBox="0 0 447 624" xmlns="http://www.w3.org/2000/svg">
    <defs>
      <linearGradient id="photoFaint" x1="0" y1="0" x2="0" y2="1">
        <stop offset="0" stop-color="#a9a888"/>
        <stop offset="0.5" stop-color="var(--photo-faint)"/>
        <stop offset="1" stop-color="#e0d6b8"/>
      </linearGradient>
    </defs>
    <rect class="photo photo-background" role="img" aria-label="Blasses Hintergrundfoto: Bike-Federgabel vor Nadelbäumen und Kiesweg" width="447" height="624" fill="url(#photoFaint)"/>

    <polygon class="info-panel" points="224,0 447,223 447,400 224,624 0,400 0,224" fill="var(--espresso)"/>
    <polyline points="0,236 224,16 447,239" fill="none" stroke="var(--sand)" stroke-width="0.6"/>
    <polyline points="0,392 224,612 447,392" fill="none" stroke="var(--sand)" stroke-width="0.6"/>

    <polygon class="corner-shape" points="0,0 48,0 90,42 45,87 0,42" fill="var(--espresso)"/>
    <polygon class="accent-diamond" points="20,96 42,118 20,140 -2,118" fill="var(--rust)"/>
    <polygon class="accent-diamond" points="405,164 428,187 405,210 382,187" fill="var(--rust)"/>
    <polygon class="accent-diamond" points="68,430 121,483 68,536 15,483" fill="var(--rust)"/>

    <text class="brand-name" x="224" y="205" text-anchor="middle">RADWERK ALPIN</text>

    <g class="info-column">
      <text class="info-text" x="20" y="261">GRATIS</text>
      <text class="info-text" x="20" y="278">FAHRTRAINING</text>
      <text class="info-text" x="20" y="312">FÜR ALLE JUGENDLICHEN</text>
      <text class="info-text" x="20" y="329">VON 8 - 14 JAHREN</text>
      <text class="info-text" x="20" y="363">JEDEN FREITAG</text>
      <text class="info-text" x="20" y="380">16:30 - 18:30</text>
    </g>
    <line x1="160" y1="252" x2="160" y2="394" stroke="var(--white)" stroke-width="2"/>
    <g class="info-column">
      <text class="info-text" x="188" y="261">LEITUNG</text>
      <text class="info-text" x="188" y="295">LINO VERHAART</text>
      <text class="info-text" x="188" y="312">LEHRLING 1. JAHR</text>
      <text class="info-text" x="188" y="346">MIT EIGENEM</text>
      <text class="info-text" x="188" y="363">BIKE GRATIS</text>
      <text class="info-text" x="188" y="397">MIT MIETBIKE</text>
      <text class="info-text" x="188" y="414">FR. 20,-</text>
    </g>
    <line x1="307" y1="252" x2="307" y2="394" stroke="var(--white)" stroke-width="2"/>
    <g class="info-column">
      <text class="info-text" x="333" y="261">BREMSTRAINING</text>
      <text class="info-text" x="333" y="295">FAHRKURSE</text>
      <text class="info-text" x="333" y="329">WHEELYTRAINING</text>
      <text class="info-text" x="333" y="363">TECHNIKTIPS</text>
      <text class="info-text" x="333" y="397">REPARATURKURSE</text>
    </g>

    <rect class="contact-band" x="38" y="548" width="372" height="48" fill="var(--rust)"/>
    <text class="contact-text" x="224" y="568" text-anchor="middle">via surlej 8   |   7590 Val Rondo</text>
    <text class="contact-text" x="224" y="586" text-anchor="middle">info@radwerkalpin.ch   |   081 000 12 34</text>
  </svg>

</main>
</body>
</html>
```